SKYWARD LENSWORKS New Wordpress Design Project

Skyward Lensworks is a photo-sharing site for aviation photographers and enthusiasts.

Please redesign the home page (http://www.skywardlensworks.example/) and photo feature page (http://www.skywardlensworks.example/2014/10/borvel-freight-23/).

We like and would like to keep the logo we have, but are open to changing colors on the logo to suit a new color scheme if necessary.
Updates

Hi All, Thank you for taking part in this design competition. Could you please show us your first round design concepts within 24hrs as we hope to show our client them and start providing feedback? Much appreciated, Lex VH BramblePeak Design

Hi All, A few tips: Could you try keep the search bar above the fold Include a section for showing new blog posts Try to integrate an ads a little better also above and below the fold Appreciated, Lex Vh

Target Market(s)

Aviation photographers and enthusiasts of all age groups globally.

Industry/Entity Type

Aviation

Requirements
Must have
• • Clean and consistent layout
• A good way to incorporate advertisements on the home page and photo feature page
• Clear and simple menu navigation
• On home page – call to action to register
• On home page - call to action to upload photos
• On home page – social buttons call to action to follow, circle, like, etc
• On photo feature page – call to action to tweet, +1, Like, etc a photo
Nice to have
• Sites we like

www.quillpane.example
http://www.layoutorchard.example/demo/45176.html
Should not have
• • Unnecessary animations
• No Adobe Flash
• Overly crowded / busy design

```html
<!DOCTYPE html>
<html lang="en">
<head>
<meta charset="utf-8">
<title>Skyward Lensworks — Home</title>
<link href="https://fonts.googleapis.com/css2?family=Open+Sans:wght@400;600;700;800&display=swap" rel="stylesheet">
<style>
  :root{
    --orange:#ee8f10;
    --ink:#1d1d1d;
    --muted:#a7a7a7;
    --rule:#e6e6e6;
    --white:#ffffff;
    --footer:#050505;
    --footer-text:#dcdcdc;
    --icon:#6d6d6d;
  }
  *{box-sizing:border-box;margin:0;padding:0}
  html,body{width:1200px;height:2715px;overflow:hidden;background:var(--white)}
  body{position:relative;font-family:"Open Sans",Arial,sans-serif;color:var(--ink)}

  /* header */
  .site-header{position:absolute;left:0;top:0;width:1200px;height:112px;background:var(--white)}
  .brand{position:absolute;left:92px;top:42px;display:flex;align-items:center;gap:10px;font-size:27px;font-weight:700;color:var(--ink);letter-spacing:-.5px}
  .brand-dot{width:14px;height:14px;border-radius:50%;background:var(--orange)}
  .main-nav a{position:absolute;top:46px;font-size:12.5px;color:#555;text-decoration:none;text-transform:uppercase;letter-spacing:.2px}
  .main-nav a.active{color:var(--orange)}
  .btn{position:absolute;display:flex;align-items:center;justify-content:center;background:var(--orange);color:var(--white);font-weight:600;text-transform:uppercase;text-decoration:none;border-radius:2px}
  .btn-register{left:1017px;top:38px;width:91px;height:38px;font-size:12px}

  /* hero */
  .hero{position:absolute;left:0;top:112px;width:1200px;height:579px;background:radial-gradient(ellipse at 62% 30%,#fff2d8 0%,#f7cf92 25%,#eca85e 55%,#c07a4e 85%,#8a5a45 100%)}
  .hero-building{position:absolute;left:0;top:0;width:410px;height:579px;background:linear-gradient(100deg,#2e2624 0%,#5e4740 50%,#8c6a57 85%,rgba(140,106,87,0) 100%)}
  .hero-plane{position:absolute;left:555px;top:45px;width:390px;height:470px;background:radial-gradient(ellipse at 50% 45%,rgba(70,60,70,.45) 0%,rgba(70,60,70,.15) 45%,rgba(70,60,70,0) 70%)}
  .hero-title{position:absolute;left:0;width:1200px;text-align:center;top:360px;font-size:37px;line-height:50px;font-weight:700;color:#111}
  .hero-sub{position:absolute;left:0;width:1200px;text-align:center;top:424px;font-size:31px;line-height:42px;color:#1a1a1a}
  .btn-upload{left:520px;top:493px;width:160px;height:51px;font-size:13px}
  .hero-next{position:absolute;left:1126px;top:375px;width:54px;height:54px;background:rgba(160,150,140,.75);display:flex;align-items:center;justify-content:center}
  .dots{position:absolute;top:705px;left:550px;display:flex;gap:4px}
  .dots span{width:11px;height:11px;border-radius:50%;border:1px solid #bbb;background:#fff}
  .dots span.on{background:var(--orange);border-color:var(--orange)}
  .rule{position:absolute;left:0;width:1200px;height:1px;background:var(--rule)}

  .section-title{position:absolute;left:0;width:1200px;text-align:center;font-size:20px;line-height:28px;font-weight:600;text-transform:uppercase}
  .section-desc{position:absolute;left:0;width:1200px;text-align:center;font-size:14px;line-height:22px;color:var(--muted)}

  .search{position:absolute;left:348px;top:885px;width:503px;height:51px;border:1px solid #ddd;display:flex;align-items:center;padding:0 16px;font-size:14px;color:#aaa;justify-content:space-between}

  .thumb{position:absolute;width:230px;height:180px;border:3px solid #fff;box-shadow:0 7px 6px -3px rgba(0,0,0,.3),0 0 2px rgba(0,0,0,.2)}
  .thumb-hover{background:linear-gradient(180deg,#9c8a5a 0%,#d59a36 35%,#d79a2e 65%,#a7742a 100%)}
  .thumb-caption{position:absolute;left:0;width:100%;bottom:12px;text-align:center;color:#fff;font-size:15px}
  .thumb-zoom{position:absolute;left:94px;top:66px;width:40px;height:40px;border-radius:50%;background:#fff}

  .btn-more{width:92px;height:38px;font-size:12px;left:554px}

  .card{position:absolute;top:1584px;width:322px;height:275px;background:#fff;box-shadow:0 0 3px rgba(0,0,0,.25),0 4px 5px rgba(0,0,0,.12)}
  .card-photo{position:absolute;left:3px;top:3px;width:316px;height:173px}
  .card-title{position:absolute;left:18px;top:193px;font-size:14px;line-height:20px;font-weight:600;color:var(--orange)}
  .card-likes{position:absolute;right:18px;top:194px;font-size:12px;color:#666;display:flex;align-items:center;gap:4px}
  .card-text{position:absolute;left:18px;top:223px;width:290px;font-size:11px;line-height:19px;color:#999}

  /* promo banner */
  .promo{position:absolute;left:0;top:1975px;width:1200px;height:282px;overflow:hidden}
  .promo-photo{position:absolute;inset:0;background:
      linear-gradient(180deg,rgba(0,0,0,0) 70%,rgba(110,110,110,.7) 100%),
      linear-gradient(90deg,#223022 0%,#3f4d36 35%,#6e786a 60%,#a3aaac 78%,#7d8577 100%)}
  .promo-badge{position:absolute;left:94px;top:27px;width:174px;height:72px;background:#1f4f9a;border:3px solid #fff;border-radius:4px;display:flex;align-items:center;padding-left:12px;color:#fff;font-size:15px;font-weight:700}
  .promo-when{position:absolute;left:295px;top:35px;color:#fff;font-size:20px;font-weight:600;line-height:28px}
  .promo-deal{position:absolute;left:90px;top:118px;height:72px;color:#fff;font-size:52px;line-height:72px;font-weight:600;white-space:nowrap}
  .promo-deal b{color:var(--orange);font-size:78px;font-weight:700;margin:0 6px}
  .promo-note{position:absolute;left:90px;top:204px;color:#fff;font-size:18px;font-weight:600;line-height:23px}
  .promo-note span{display:block;padding-left:333px}
  .promo-arrow{position:absolute;top:124px;width:36px;height:36px;border-radius:50%;border:2px solid #fff;background:rgba(0,0,0,.2)}

  .btn-account{left:483px;top:2425px;width:234px;height:49px;font-size:15px}

  .site-footer{position:absolute;left:0;top:2534px;width:1200px;height:181px;background:var(--footer)}
  .footer-links{position:absolute;top:32px;left:0;width:1200px;text-align:center;color:#fff;font-size:11px;letter-spacing:.3px}
  .footer-links i{font-style:normal;margin:0 8px}
  .copyright{position:absolute;top:75px;left:0;width:1200px;text-align:center;color:var(--footer-text);font-size:11px}
  .copyright a{color:var(--orange);text-decoration:none}
  .social{position:absolute;top:120px;left:529px;display:flex;gap:8px}
  .social span{width:30px;height:30px;background:var(--icon);border-radius:3px}
  .footer-bar{position:absolute;left:0;bottom:0;width:1200px;height:6px;background:var(--orange)}
</style>
</head>
<body>

<header class="site-header">
  <div class="brand"><span class="brand-dot"></span>Skyward Lensworks</div>
  <nav class="main-nav">
    <a class="active" href="#" style="left:513px">Home</a>
    <a href="#" style="left:585px">Photos</a>
    <a href="#" style="left:670px">Submit a Photo</a>
    <a href="#" style="left:811px">Airport Search</a>
    <a href="#" style="left:949px">Login</a>
  </nav>
  <a class="btn btn-register" href="#">Register</a>
</header>

<section class="hero" role="img" aria-label="Airliner flying over a glass office tower at sunset">
  <div class="hero-building"></div>
  <div class="hero-plane"></div>
</section>
<h1 class="hero-title">Be Inspired. Get Discovered.</h1>
<p class="hero-sub">Join the premier photography community.</p>
<a class="btn btn-upload" href="#">Upload Photos</a>
<div class="hero-next"><svg width="20" height="24" viewBox="0 0 20 24"><path d="M5 3 L15 12 L5 21" fill="none" stroke="#fff" stroke-width="4"/></svg></div>
<div class="dots"><span></span><span></span><span></span><span class="on"></span><span></span><span></span><span></span></div>
<div class="rule" style="top:728px"></div>

<h2 class="section-title" style="top:771px">Top Photos</h2>
<p class="section-desc" style="top:816px">Browse our incredible collection of licensable photos<br>submitted by the Quillpane community.</p>
<div class="search">Search
  <svg width="26" height="26" viewBox="0 0 26 26"><circle cx="10" cy="10" r="7" fill="none" stroke="#ee8f10" stroke-width="3"/><path d="M15 15 L23 23" stroke="#ee8f10" stroke-width="4" stroke-linecap="round"/></svg>
</div>

<div class="thumb" role="img" aria-label="White airliner taxiing on a runway" style="left:96px;top:981px;background:linear-gradient(180deg,#2f4a27 0%,#5f7d44 35%,#9ba08c 55%,#7c7c7a 80%,#5f5f5f 100%)"></div>
<div class="thumb thumb-hover" role="img" aria-label="Yellow painted airliner on the apron" style="left:355px;top:981px">
  <div class="thumb-zoom"></div><div class="thumb-caption">Neque Porro</div></div>
<div class="thumb" role="img" aria-label="Business jet flying in blue sky" style="left:614px;top:981px;background:linear-gradient(160deg,#2f7fd6 0%,#6aa7e6 45%,#d8e7f4 70%,#7fb2e4 100%)"></div>
<div class="thumb" role="img" aria-label="Red-tailed airliner landing past a control tower" style="left:874px;top:981px;background:linear-gradient(180deg,#d1dbe6 0%,#bdc8d4 55%,#8e9499 80%,#6f7376 100%)"></div>
<div class="thumb" role="img" aria-label="Turboprop aircraft on the runway" style="left:96px;top:1194px;background:linear-gradient(180deg,#4c5a3c 0%,#7f8b63 35%,#b8b8b2 55%,#8a8a8a 80%,#6a6a6a 100%)"></div>
<div class="thumb" role="img" aria-label="Jumbo jet parked in front of trees" style="left:355px;top:1194px;background:linear-gradient(180deg,#c8d2da 0%,#2f4f31 30%,#3f6a40 45%,#6fb0bd 62%,#8b8f92 82%,#555 100%)"></div>
<div class="thumb" role="img" aria-label="Regional airliner taxiing" style="left:614px;top:1194px;background:linear-gradient(180deg,#2a3a26 0%,#4f6140 35%,#c9c9c4 55%,#8f8f8f 80%,#666 100%)"></div>
<div class="thumb" role="img" aria-label="White airliner rolling on the runway" style="left:874px;top:1194px;background:linear-gradient(180deg,#2d4a28 0%,#5b7a48 35%,#c4c4c6 55%,#979797 80%,#6e6e6e 100%)"></div>

<a class="btn btn-more" href="#" style="top:1423px">More</a>
<div class="rule" style="top:1499px"></div>

<h2 class="section-title" style="top:1533px">All Most Viewed</h2>

<article class="card" style="left:92px">
  <div class="card-photo" role="img" aria-label="Vintage propeller fighter aircraft on grass" style="background:linear-gradient(180deg,#3d8ad4 0%,#8fbbe0 35%,#5e6a55 60%,#a08b3e 80%,#6a6030 100%)"></div>
  <h3 class="card-title">Neque porro quisquam est</h3>
  <span class="card-likes"><svg width="11" height="10" viewBox="0 0 11 10"><path d="M5.5 10 L0.8 5 A2.6 2.6 0 0 1 5.5 1.6 A2.6 2.6 0 0 1 10.2 5 Z" fill="#555"/></svg>Likes</span>
  <p class="card-text">Sed ut perspiciatis unde omnis iste natus error sit accusantium doloremque laudantium,</p>
</article>
<article class="card" style="left:440px">
  <div class="card-photo" role="img" aria-label="Red and white floatplane on the tarmac" style="background:linear-gradient(180deg,#c4d0dc 0%,#9aa5b2 30%,#c9443a 50%,#e6e6e6 62%,#4f5a4e 80%,#707070 100%)"></div>
  <h3 class="card-title">Neque porro quisquam est</h3>
  <span class="card-likes"><svg width="11" height="10" viewBox="0 0 11 10"><path d="M5.5 10 L0.8 5 A2.6 2.6 0 0 1 5.5 1.6 A2.6 2.6 0 0 1 10.2 5 Z" fill="#555"/></svg>Likes</span>
  <p class="card-text">Sed ut perspiciatis unde omnis iste natus error sit accusantium doloremque laudantium,</p>
</article>
<article class="card" style="left:787px">
  <div class="card-photo" role="img" aria-label="Widebody airliner climbing in a grey sky" style="background:linear-gradient(160deg,#aeb8c2 0%,#c8cfd6 40%,#eef0f2 55%,#c0c8d0 75%,#b4bdc6 100%)"></div>
  <h3 class="card-title">Neque porro quisquam est</h3>
  <span class="card-likes"><svg width="11" height="10" viewBox="0 0 11 10"><path d="M5.5 10 L0.8 5 A2.6 2.6 0 0 1 5.5 1.6 A2.6 2.6 0 0 1 10.2 5 Z" fill="#555"/></svg>Likes</span>
  <p class="card-text">Sed ut perspiciatis unde omnis iste natus error sit accusantium doloremque laudantium,</p>
</article>

<a class="btn btn-more" href="#" style="top:1891px">More</a>

<section class="promo">
  <div class="promo-photo" role="img" aria-label="Airliner on a runway with green hills behind"></div>
  <div class="promo-badge">Northgate Bank</div>
  <p class="promo-when">ONLY ON<br>WEDNESDAY’S</p>
  <p class="promo-deal">Upto<b>50%</b>Off</p>
  <p class="promo-note">Additional Discount on&nbsp; Domestic flight booking<span>(Base for only)</span></p>
  <svg class="promo-arrow" style="left:18px" viewBox="0 0 36 36"><path d="M21 10 L13 18 L21 26" fill="none" stroke="#fff" stroke-width="3"/></svg>
  <svg class="promo-arrow" style="left:1133px" viewBox="0 0 36 36"><path d="M15 10 L23 18 L15 26" fill="none" stroke="#fff" stroke-width="3"/></svg>
</section>

<h2 class="section-title" style="top:2312px">Join Skyward Lensworks</h2>
<p class="section-desc" style="top:2356px;font-size:15px">Sed ut perspiciatis unde omnis iste natus error sit voluptatem accusantium<br>doloremque laudantium, totam rem aperiam, eaque ipsa quae ab</p>
<a class="btn btn-account" href="#">Create an Account</a>

<footer class="site-footer">
  <p class="footer-links">SEARCH<i>|</i>CALENDAR<i>|</i>ABOUT<i>|</i>DONATION<i>|</i>PRIVACY</p>
  <p class="copyright">Copyright Skyward Lensworks (C) - All rights reserved. &nbsp;|&nbsp; <a href="#">Site Credit</a></p>
  <div class="social" aria-label="Follow us"><span></span><span></span><span></span><span></span></div>
  <div class="footer-bar"></div>
</footer>

</body>
</html>
```